Design for a real estate wev portal

Contents and features of the site
---------------------------------
Website in 5 languages: French, Dutch, English, German, Spanish.
English name of the site: Lantern Nest Living
Main purpose of the site:
- allow people to rent their house/ appartment for flatsharing purposes.
- help people wanting to find a room in flatsharing
- help people to find additional roommates for their flatsharing
Key interaction sequence:
1. I create a "group" of people who have common interest/hobbies
2. People who have the same interests/hobbies join my group
3. I look for a house/appartment to host my group
Website structure will be the following:
- Home
- Groups
-- Look for a group
--- Join a group
-- Create a group
- Properties
-- Look for a house/appartement
-- Apply
- Sales conditions
- Contact
- My account
-- My profile
-- My groups OR my properties
Your mission
------------
The client has no graphical guidelines, simply a logo (see attached).
We need a (responsive compliant) design for the following pages (we expect PSD's from you. No HTML nor CSS):
1. homepage (see example and wireframe attached)
2. properties search result list (see wireframe attached)
3. "detailed" form for properties
4. groups search result list
5. "detailed" form for groups
6. my account page
FOR THE COMPETITION step we only expect from you the design of first 2 screens.
Based on that, we will select the designer who will win the project, and will have to design the 4 remaining screens.
Target Market(s)
B2C
Industry/Entity Type
Real Estate
Number of Pages Required
5+ page
Look and feel
Each slider illustrates characteristics of the customer's brand and the style your logo design should communicate.

```html
<!DOCTYPE html>
<html lang="en">
<head>
<meta charset="utf-8">
<title>Lantern Nest Living – Home</title>
<link rel="stylesheet" href="https://fonts.googleapis.com/css2?family=Montserrat:wght@400;500;600&family=Open+Sans:wght@400;600;700&display=swap">
<style>
:root{
  --teal:#1697a8;
  --teal-soft:#86cfd8;
  --teal-band:#9dd8df;
  --teal-card:#d6f4f8;
  --green:#6abd45;
  --green-soft:#b3e0a1;
  --green-band:#c3e8b3;
  --green-card:#e3f7d9;
  --paper:#f4f3f0;
  --ink:#222;
  --body:#333;
  --muted:#666;
  --line:#dcdcdc;
  --white:#fff;
}
*{box-sizing:border-box;margin:0;padding:0}
html,body{width:1200px;height:2624px;overflow:hidden}
body{position:relative;font-family:"Open Sans",Arial,sans-serif;color:var(--body);background:var(--paper)}
.abs{position:absolute}
.head{font-family:"Montserrat",Arial,sans-serif}

/* header */
.site-header{position:absolute;left:0;top:0;width:1200px;height:126px;background:var(--white)}
.phone{left:100px;top:29px;font-size:14px;color:var(--ink)}
.main-nav{left:100px;top:74px;display:flex;gap:0;font-family:"Montserrat",Arial,sans-serif;font-size:13px;font-weight:500;color:var(--ink)}
.main-nav span{position:absolute;white-space:nowrap}
.main-nav .active{color:var(--green)}
.brand{left:505px;top:38px;width:200px;height:56px;display:flex;align-items:center;gap:10px}
.brand-dot{width:20px;height:20px;border-radius:50%;background:var(--green);flex:none}
.brand-name{font-family:"Open Sans",Arial,sans-serif;font-weight:700;font-size:20px;line-height:1.05;color:#2b4a55}
.account-links{right:98px;top:24px;font-size:13px;color:var(--ink);word-spacing:2px}
.lang{left:1010px;top:66px;width:90px;height:34px;border:1px solid #ccc;font-size:11px;display:flex;align-items:center;justify-content:center;gap:6px;color:var(--ink)}
.lang .flag{width:12px;height:8px;background:#c8283c}

/* hero */
.hero-side{top:126px;height:430px;width:600px}
.hero-left{left:0;background:var(--teal-soft)}
.hero-right{left:600px;background:var(--green-soft)}
.hero-band{position:absolute;left:0;top:0;width:100%;height:84px;display:flex;align-items:center;justify-content:center;font-family:"Montserrat",Arial,sans-serif;font-size:24px;font-weight:500;color:var(--white);letter-spacing:.3px}
.hero-left .hero-band{background:var(--teal-band)}
.hero-right .hero-band{background:var(--green-band)}
.choice{position:absolute;top:236px;width:236px;height:264px}
.choice .photo{height:190px}
.choice .label{height:74px;padding:16px 18px;font-size:16px;line-height:1.35;color:var(--ink)}
.teal-card .label{background:var(--teal-card)}
.green-card .label{background:var(--green-card)}

/* spotlight */
.section-title{font-family:"Montserrat",Arial,sans-serif;font-size:25px;font-weight:500;color:var(--ink)}
.spot{position:absolute;height:187px;background:var(--white);border:1px solid var(--line);display:flex}
.spot .photo{width:201px;height:100%;flex:none}
.spot .info{padding:10px 14px;font-size:12px;line-height:21px;color:var(--body)}
.spot h3{font-family:"Montserrat",Arial,sans-serif;font-size:16px;font-weight:500;color:var(--ink);margin:4px 0 4px 6px}
.btn{position:absolute;height:40px;display:flex;align-items:center;justify-content:center;font-family:"Montserrat",Arial,sans-serif;font-size:13px;font-weight:600;color:var(--white)}
.btn-green{background:var(--green)}
.btn-teal{background:var(--teal)}

/* selling points */
.ksp{top:1214px;width:600px;height:444px}
.ksp-left{left:0;background:var(--teal)}
.ksp-right{left:600px;background:var(--green)}
.ksp h2{position:absolute;top:86px;font-family:"Montserrat",Arial,sans-serif;font-size:25px;font-weight:500;color:var(--white);line-height:30px}
.ksp p{position:absolute;top:164px;font-size:12px;line-height:21.5px;color:var(--white)}
.ksp-ring{position:absolute;width:110px;height:110px;border-radius:50%;background:rgba(255,255,255,.07)}

/* faq */
.faq{position:absolute;left:98px;width:1002px;height:86px;background:var(--white);border:1px solid var(--line)}
.faq svg{position:absolute;left:-1px;top:-1px}
.faq .num{position:absolute;left:12px;top:8px;font-family:"Montserrat",Arial,sans-serif;font-size:19px;font-weight:500;color:var(--white)}
.faq p{position:absolute;left:62px;right:20px;top:20px;font-size:12px;line-height:21px;color:var(--ink)}
.faq .more{color:var(--green);font-weight:600}

/* tool bands */
.tool{top:2181px;width:600px;height:77px;display:flex;align-items:center;justify-content:center;gap:16px;font-family:"Montserrat",Arial,sans-serif;font-size:20px;font-weight:500;color:var(--white)}
.tool-left{left:0;background:var(--teal)}
.tool-right{left:600px;background:var(--green)}

/* footer */
.site-footer{position:absolute;left:0;top:2258px;width:1200px;height:366px;background:var(--white);overflow:hidden}
.foot-ring{position:absolute;border-radius:50%;background:#f3f3f3}
.foot-brand{left:98px;top:72px;display:flex;align-items:center;gap:10px}
.foot-about{left:102px;top:160px;width:240px;font-size:12px;line-height:22px;color:var(--ink)}
.foot-col{position:absolute;top:66px;font-size:12px;line-height:24px;color:var(--ink)}
.foot-col h4{font-family:"Montserrat",Arial,sans-serif;font-size:15px;font-weight:500;margin-bottom:8px;color:var(--ink)}
.foot-rule{left:98px;top:278px;width:1002px;height:1px;background:#e3e3e3}
.copyright{left:100px;top:316px;font-size:11.5px;color:var(--ink);word-spacing:1px}
.social{position:absolute;top:310px;width:32px;height:32px;border-radius:50%}
</style>
</head>
<body>

<header class="site-header">
  <div class="abs phone">Call Us: 555-014-2290</div>
  <nav class="abs main-nav">
    <span class="active" style="left:0">HOME</span>
    <span style="left:82px">SERVICES</span>
    <span style="left:187px">ROOMS</span>
    <span style="left:280px">CONTACT</span>
  </nav>
  <div class="abs brand">
    <span class="brand-dot"></span>
    <span class="brand-name">Lantern Nest<br>Living</span>
  </div>
  <div class="abs account-links">Create &nbsp;|&nbsp; Login &nbsp;|&nbsp; My Account</div>
  <div class="abs lang"><span class="flag"></span>English ▾</div>
</header>

<section class="abs hero-side hero-left">
  <div class="hero-band">SEARCHING FOR ACCOMMODATION</div>
</section>
<section class="abs hero-side hero-right">
  <div class="hero-band">I HAVE A HOUSE FOR RENT</div>
</section>

<a class="choice teal-card" style="left:98px">
  <div class="photo" role="img" aria-label="Photo of a bright living room with a fireplace" style="background:linear-gradient(160deg,#e9e1d4,#a8937a)"></div>
  <div class="label">I want to rent a room<br>Right now !</div>
</a>
<a class="choice teal-card" style="left:348px">
  <div class="photo" role="img" aria-label="Photo of young roommates sitting together" style="background:linear-gradient(160deg,#f1efed,#c9b8a8)"></div>
  <div class="label">I want to<br>Join a Group</div>
</a>
<a class="choice green-card" style="left:614px">
  <div class="photo" role="img" aria-label="Photo of a furnished bedroom with a teal bedspread" style="background:linear-gradient(160deg,#f0eeea,#5aa6a8)"></div>
  <div class="label">I want to<br>Advertise !</div>
</a>
<a class="choice green-card" style="left:864px">
  <div class="photo" role="img" aria-label="Photo of friends sharing a meal at a table" style="background:linear-gradient(160deg,#7b8f6a,#3e3a3a)"></div>
  <div class="label">Why is flatsharing<br>interesting for me ?</div>
</a>

<h2 class="abs section-title" style="left:98px;top:618px">UNDER THE SPOTLIGHT</h2>
<h2 class="abs section-title" style="left:609px;top:618px">UNDER THE SPOTLIGHT</h2>

<article class="spot" style="left:98px;top:682px;width:490px">
  <div class="photo" role="img" aria-label="Photo of a group of young people with luggage" style="background:linear-gradient(160deg,#8a8c6e,#b54a3a)"></div>
  <div class="info">
    <h3>A NICE GROUP</h3>
    Consectetuer adipiscing elit, sed diam nonu<br>mmy nibh euismod tincidun.<br>oung workers, seeking for accomodation<br>downtown.<br>Average age: 35<br>Men and women welcome
  </div>
</article>
<article class="spot" style="left:98px;top:897px;width:490px">
  <div class="photo" role="img" aria-label="Photo of two young women looking at a phone" style="background:linear-gradient(160deg,#d9cbbb,#8a5a3e)"></div>
  <div class="info">
    <h3>ANOTHER NICE GROUP</h3>
    Consectetuer adipiscing elit, sed diam nonu<br>mmy nibh euismod tincidunt.<br>Young ladies, studying at Riverside University seeking for<br>accomodation close to Riverside University.<br>Average age: 20 Y<br>Only Women
  </div>
</article>
<article class="spot" style="left:609px;top:682px;width:491px">
  <div class="photo" role="img" aria-label="Photo of a large house with a green lawn" style="background:linear-gradient(180deg,#8fb8d8 0%,#b9b6a8 50%,#4f9a3a 100%)"></div>
  <div class="info">
    <h3>HOUSE</h3>
    Consectetuer adiploiscing elit, sed diam nonu<br>mmy nibh euismod tincinsectetuer adiploiscin<br>elitsed diamismod tincinsectetu.<br>Town:<br>Rent per month:<br>Availability:
  </div>
</article>
<article class="spot" style="left:609px;top:897px;width:491px">
  <div class="photo" role="img" aria-label="Photo of a bedroom with wooden floor" style="background:linear-gradient(180deg,#e4e1dc 0%,#cfc9c0 60%,#6e3f24 100%)"></div>
  <div class="info">
    <h3>APPARTMENT</h3>
    Consectetuer adiploiscing elit, sed diam nonu<br>mmy nibh euismod tincinsectetuer adiploiscin<br>elitsed diamismod tincinsectetu.<br>Town:<br>Rent per month:<br>Availability:
  </div>
</article>

<a class="btn btn-green" style="left:98px;top:1116px;width:184px">SEE MORE GROUPS&nbsp;»</a>
<a class="btn btn-teal" style="left:610px;top:1116px;width:184px">SEE MORE HOUSES&nbsp;»</a>

<section class="abs ksp ksp-left">
  <div class="ksp-ring" style="left:250px;top:230px"></div>
  <h2 style="left:98px">KEY SELLING POINTS<br>FOR THE ROOMMATES</h2>
  <p style="left:98px;width:452px">Consectetuer adipiscing elit, sed diam nonummy nibh euismod tincidunt ut laore et dolore magna aliquam erat volutpat. Ut wisi enim ad minim veniam, quis nost rud exerci tation ullamcorper suscipit lobortis nisi ut aliquip ex ea commodo con diam nonummy nibh euismod tincidunt ut laoreet dolore seqonsectetuer adipisc ing elit, sed diam nonummy nibh euismod tincidunt ut laoreet dolore magna ali am erat volutpat. Ut wisi enim ad minim veniam, quis nostrud exerci tation ullam corper suscipit lobortis nisi ut aliquip ex ea commodo con diam nonummy nibh euismod tincidunt ut laoreet dolore sequa.</p>
</section>
<section class="abs ksp ksp-right">
  <div class="ksp-ring" style="left:250px;top:230px"></div>
  <h2 style="left:48px">KEY SELLING POINTS<br>FOR THE OWNERS</h2>
  <p style="left:48px;width:452px">Consectetuer adipiscing elit, sed diam nonummy nibh euismod tincidunt ut laore et dolore magna aliquam erat volutpat. Ut wisi enim ad minim veniam, quis nost rud exerci tation ullamcorper suscipit lobortis nisi ut aliquip ex ea commodo con diam nonummy nibh euismod tincidunt ut laoreet dolore seqonsectetuer adipisc ing elit, sed diam nonummy nibh euismod tincidunt ut laoreet dolore magna ali am erat volutpat. Ut wisi enim ad minim veniam, quis nostrud exerci tation ullam corper suscipit lobortis nisi ut aliquip ex ea commodo con diam nonummy nibh euismod tincidunt ut laoreet dolore sequa.</p>
</section>

<h2 class="abs section-title" style="left:0;width:1200px;top:1734px;text-align:center">EVERYTHING YOU NEED TO KNOW ABOUT FLATSHARING</h2>

<article class="faq" style="top:1801px">
  <svg width="84" height="86" viewBox="0 0 84 86"><path d="M0 0H84L0 74Z" fill="#6abd45"/></svg>
  <span class="num">01</span>
  <p>Consectetuer adipiscing elit, sed diam nonummy nibh euismod tincidunt ut laoreet dolore magna aliquam erat volutpat. Ut wisi enim ad minim veniam, quis nostrud exerci tation ullamcorper suscipit lobortis nisi ut aliquip ex ea commodo con diam nonummy nibh euismod tincidunt ut laoreet dolore sequa. <span class="more">Read More</span></p>
</article>
<article class="faq" style="top:1901px">
  <svg width="84" height="86" viewBox="0 0 84 86"><path d="M0 0H84L0 74Z" fill="#6abd45"/></svg>
  <span class="num">02</span>
  <p>Consectetuer adipiscing elit, sed diam nonummy nibh euismod tincidunt ut laoreet dolore magna aliquam erat volutpat. Ut wisi enim ad minim veniam, quis nostrud exerci tation ullamcorper suscipit lobortis nisi ut aliquip ex ea commodo con diam nonummy nibh euismod tincidunt ut laoreet dolore sequa. <span class="more">Read More</span></p>
</article>
<article class="faq" style="top:1999px">
  <svg width="84" height="86" viewBox="0 0 84 86"><path d="M0 0H84L0 74Z" fill="#6abd45"/></svg>
  <span class="num">03</span>
  <p>Consectetuer adipiscing elit, sed diam nonummy nibh euismod tincidunt ut laoreet dolore magna aliquam erat volutpat. Ut wisi enim ad minim veniam, quis nostrud exerci tation ullamcorper suscipit lobortis nisi ut aliquip ex ea commodo con diam nonummy nibh euismod tincidunt ut laoreet dolore sequa. <span class="more">Read More</span></p>
</article>

<a class="btn btn-teal" style="left:943px;top:2104px;width:157px">ALL QUESTIONS&nbsp;»</a>

<a class="abs tool tool-left">
  <svg width="42" height="46" viewBox="0 0 42 46" fill="none" stroke="#fff" stroke-width="2.5"><path d="M4 20L21 4L38 20V42H4Z"/><circle cx="20" cy="27" r="7"/><path d="M25 32L31 38"/></svg>
  PRE-DEFINED SEARCHES
</a>
<a class="abs tool tool-right">
  <svg width="42" height="42" viewBox="0 0 42 42" fill="none" stroke="#fff" stroke-width="2.5"><circle cx="16" cy="24" r="13"/><path d="M16 19V31M16 15V16"/><path d="M24 12A10 10 0 1 1 34 24"/></svg>
  TOOLS AND INFORMATIONS
</a>

<footer class="site-footer">
  <div class="foot-ring" style="left:910px;top:150px;width:130px;height:130px"></div>
  <div class="foot-ring" style="left:958px;top:180px;width:166px;height:166px"></div>
  <div class="abs foot-brand">
    <span class="brand-dot"></span>
    <span class="brand-name">Lantern Nest<br>Living</span>
  </div>
  <p class="abs foot-about">Sed ut perspiciatis unde omnis iste nat us erlorior sit volup ptatem accusantium dolo remque laudantium, totam.</p>
  <div class="foot-col" style="left:402px"><h4>Links</h4>Sed ut perspiciatis<br>Qnde omnis iste n<br>Wtus error sit voluptat<br>em accusantiu<br>Gdoloremque</div>
  <div class="foot-col" style="left:607px"><h4>Let Us Help You</h4>Your Account<br>Your Orders<br>Sed ut perspiciatis nde<br>Wtus error sit voluptat<br>Saccusantiu<br>Gdoloremque</div>
  <div class="foot-col" style="left:815px"><h4>Product</h4>Sed ut perspiciatis<br>Qnde omnis iste n<br>Wtus error sit voluptat<br>em accusantiu<br>Gdoloremque</div>
  <div class="foot-col" style="left:1018px"><h4>Company</h4>Company info<br>News<br>Flatsharing<br>Sed ut perspici<br>em accusantiu<br>Policies</div>
  <div class="abs foot-rule"></div>
  <div class="abs copyright">Copyright © 2016 Lantern Nest Living. Terms of Use &nbsp; Privacy Policy &nbsp; Sitemap &nbsp; Contact Us</div>
  <span class="social" style="left:960px;background:#3fa9d8"></span>
  <span class="social" style="left:997px;background:#2d5f9a"></span>
  <span class="social" style="left:1034px;background:#1b6fa0"></span>
  <span class="social" style="left:1070px;background:#d34836"></span>
</footer>

</body>
</html>
```